Vantoralis 'Private Prism' Book Cover Design project

I need to revise the book cover design I have for my coming book. The design I created through CraftHerd is great but the book has grown and changed so I'm looking for an alternative/option design. I can then choose later from the different options.

I need a book cover that represents the unique book I am creating.

Book Title:
Your True Spectrum

Subtitle: Walking Your Path and Not Your Tag

The book is targeting all readers with a special focus on same sex attracted readers. It should not have stereotypical images.

I am including a file of the book cover I have had designed. The back cover blurb, author info and author pic will remain the same. The colouring of the back cover and spine will, of course, change to match the colouring of the front cover.

The new title will be on the spine and the new title wording.

The front cover will be markedly different using the bold images and rainbow colours of the images found in the files I am uploading for you.

I am thinking of a large boldly coloured rainbow face with the title and subtitle ON the image. The image will be the whole cover. It will fill the cover as much as possible with the text added onto the pic.

The bold pictures I am including will give you the idea of what I'm looking for.

ANY of the images I've uploaded can be used as the actual front cover image OR the designer might have/find some suitable image to be used. The image is to be large and bold and fill the cover. Hopefully a positive energy.
It needs to be eye-catching and striking and bold and positive.

So...the book cover sample file I've provided can keep the back cover with completely new colouring. The front cover is completely new with new image, wording and energy.

It is to be a rainbow coloured face or figure for the cover image.

I hope that is clear enough for you. I'm very happy to discuss and clarify these ideas with the designer. Looking forward to another great CraftHerd experience.

Target Market(s)

Wide audience with special focus on Same Sex Attracted individuals

Font styles to use
Script
Other font styles liked:
• Some form of handwriting font to make the book title and text appear more personal....as if handwritten by me.

Requirements
Must have
• Boldness, Quirky, Rainbow Colour, Image to fill the cover, maybe dark cover contrasting background.
Nice to have
• A well balanced back cover especially in the area where the barcode will be placed.
Should not have
• No stereotypical images

```html
<!DOCTYPE html>
<html lang="en">
<head>
<meta charset="utf-8">
<title>Your True Spectrum – Book Cover</title>
<link rel="stylesheet" href="https://fonts.googleapis.com/css2?family=Gochi+Hand&family=Open+Sans:ital,wght@0,400;0,700;1,400;1,700&family=Source+Sans+3:wght@600;700&display=swap">
<style>
  :root {
    --stage: #2d2066;
    --cover-orange: #fe3f12;
    --paper: #f7f7f5;
    --ink-light: #ffffff;
    --frame-line: rgba(255,255,255,0.35);
    --hand: "Gochi Hand", cursive;
    --body: "Open Sans", sans-serif;
    --heading: "Source Sans 3", sans-serif;
  }
  * { box-sizing: border-box; margin: 0; padding: 0; }
  html, body { width: 1200px; height: 1200px; overflow: hidden; }
  body { background: var(--stage); position: relative; font-family: var(--body); color: var(--ink-light); }

  .wraparound {
    position: absolute; left: 50px; top: 218px;
    width: 1102px; height: 764px; display: flex;
    outline: 1px solid var(--frame-line);
  }

  /* Back cover */
  .back-cover {
    position: relative; width: 509px; height: 100%;
    background: var(--cover-orange); padding: 62px 54px 0 54px;
    border-right: 1px solid var(--frame-line);
  }
  .back-headline {
    font-weight: 700; font-size: 12.2px; line-height: 22.4px;
    text-align: center; text-transform: uppercase; letter-spacing: 0.2px;
  }
  .back-tagline {
    margin-top: 11px; font-style: italic; font-weight: 700; font-size: 15.2px; line-height: 17px;
  }
  .back-tagline-sub { font-size: 11.2px; line-height: 13px; }
  .back-body {
    margin-top: 12px; font-size: 11.3px; line-height: 16.5px; text-align: justify;
  }
  .back-body + .back-body { margin-top: 10px; }
  .author-quote {
    margin-top: 13px; border: 1.5px solid var(--ink-light);
    padding: 7px 16px 8px 13px; font-style: italic; font-size: 12.4px; line-height: 16.3px;
  }
  .author-quote cite { display: block; text-align: right; font-weight: 700; font-size: 12.4px; margin-top: 1px; }
  .back-closing { margin-top: 13px; font-size: 11.8px; line-height: 12px; }

  .author-block { position: absolute; left: 54px; top: 546px; display: flex; gap: 6px; }
  .author-photo {
    width: 167px; height: 92px;
    background: linear-gradient(135deg, #3c5a2a 0%, #5d7d3b 45%, #2f3f22 100%);
  }
  .author-bio { font-size: 11.4px; line-height: 12.8px; }
  .author-bio .bio-name { font-family: var(--heading); font-weight: 700; font-size: 15px; line-height: 15px; }
  .author-bio .bio-web { font-weight: 700; font-size: 14px; line-height: 18px; margin-top: 1px; }

  .publisher-mark {
    position: absolute; left: 73px; top: 656px; width: 126px; height: 82px;
    display: flex; align-items: center; justify-content: center; gap: 6px;
  }
  .publisher-mark .mark-square { width: 10px; height: 10px; background: var(--ink-light); }
  .publisher-mark .mark-name { font-weight: 700; font-size: 15px; letter-spacing: 0.3px; }
  .barcode-space {
    position: absolute; left: 312px; top: 657px; width: 130px; height: 72px; background: #ffffff;
  }

  /* Spine */
  .spine {
    position: relative; width: 84px; height: 100%; background: var(--cover-orange);
  }
  .spine-title, .spine-author {
    position: absolute; left: 50%; white-space: nowrap;
    transform-origin: left center; transform: rotate(90deg) translateY(-50%);
  }
  .spine-title { top: 72px; font-family: var(--hand); font-size: 40px; line-height: 1; }
  .spine-author { top: 518px; font-family: var(--heading); font-weight: 700; font-size: 25px; letter-spacing: 1.5px; line-height: 1; }

  /* Front cover */
  .front-cover { position: relative; width: 509px; height: 100%; background: var(--paper); overflow: hidden; }
  .cover-art {
    position: absolute; left: 67px; top: 70px; width: 376px; height: 624px;
    background:
      radial-gradient(ellipse at 60% 25%, rgba(245,230,60,0.55), transparent 45%),
      radial-gradient(ellipse at 35% 55%, rgba(240,120,170,0.55), transparent 50%),
      radial-gradient(ellipse at 70% 80%, rgba(200,20,10,0.6), transparent 55%),
      #fd4a14;
    box-shadow:
      0 -34px 40px -6px rgba(210,255,120,0.55),
      34px 0 40px -6px rgba(255,140,220,0.55),
      0 34px 40px -6px rgba(230,255,90,0.6),
      -34px 0 40px -6px rgba(130,220,255,0.5);
  }
  .front-title {
    position: absolute; left: 67px; top: 196px; width: 376px;
    font-family: var(--hand); font-weight: 400; font-size: 72px; line-height: 110px;
    text-transform: uppercase; text-align: center; white-space: nowrap;
  }
  .front-title .title-line-2 { display: block; }
  .front-subtitle {
    position: absolute; left: 67px; top: 402px; width: 376px; text-align: center;
    font-family: var(--heading); font-weight: 600; font-size: 21px; white-space: nowrap;
  }
  .front-rule {
    position: absolute; left: 122px; top: 455px; width: 266px; height: 3px; background: var(--ink-light);
  }
  .front-author {
    position: absolute; left: 67px; top: 641px; width: 376px; text-align: center;
    font-family: var(--heading); font-weight: 700; font-size: 49px; line-height: 1; letter-spacing: 0.5px;
  }
</style>
</head>
<body>
  <main class="wraparound">
    <section class="back-cover">
      <p class="back-headline">It’s important to challenge our accepted beliefs and the stories we tell ourselves, individually and as a community, if there is to be any sense of wholeness, happiness and future.</p>
      <p class="back-tagline">Your Spectrum is much more than the flag you wave.</p>
      <p class="back-tagline-sub">It is the unique and individual YOU behind the layers, labels and stories.</p>
      <p class="back-body">This first book by Rowan Ashby asks each of us to consider our accepted beliefs and personal stories as we explore the possible ways to WALK OUR PATH AND NOT A TAG. Doing this require some honest inner work and a journey that will need to be passionately personal and authentically individual.</p>
      <p class="back-body">‘Your Inner Spectrum’ reminds us that a beautiful, colourful life is more than sexuality, personality or gender or having a camp, team or tribe to belong to. It is much more than any acronym, scene or lifestyle. It’s ‘an inside job’, deeply heartfelt and courageously unique. Finding and living the YOU of YOU has boldness and power and magic in it.</p>
      <blockquote class="author-quote">“Living a meaningful, happy existence is about being true to the whole, complex, integrated person that you are and being strong enough and aware enough and reflective enough to know yourself, love yourself and be yourself”<cite>Rowan Ashby</cite></blockquote>
      <p class="back-closing">This simple and insightful book will help you explore ways to bravely and honestly know, love and be yourself no matter what the rest of the scene, or world, might be doing or saying or expecting.</p>

      <div class="author-block">
        <div class="author-photo" role="img" aria-label="Portrait photo of the author seated by a tree in a garden"></div>
        <div class="author-bio">
          <p class="bio-name">Rowan Ashby</p>
          <p>Personal Change and Relationships Coach<br>VANTORALIS Coaching and Wellness<br>Advocate, Activist, Writer and support<br>for MEN WHO DATE MEN and their<br>Wholeness, Happiness and Human Rights.</p>
          <p class="bio-web">www.vantoralis.com</p>
        </div>
      </div>

      <div class="publisher-mark">
        <span class="mark-square"></span>
        <span class="mark-name">VANTORALIS</span>
      </div>
      <div class="barcode-space"></div>
    </section>

    <section class="spine">
      <p class="spine-title">YOUR TRUE SPECTRUM</p>
      <p class="spine-author">ROWAN ASHBY</p>
    </section>

    <section class="front-cover">
      <div class="cover-art" role="img" aria-label="Expressive painting of a figure in bold orange, pink, yellow and red brushstrokes"></div>
      <h1 class="front-title">Your True<span class="title-line-2">Spectrum</span></h1>
      <p class="front-subtitle">Walking Your Path and Not Your Tag</p>
      <div class="front-rule"></div>
      <p class="front-author">ROWAN ASHBY</p>
    </section>
  </main>
</body>
</html>
```